Chatterly News Feed Advertisement for Bitcoin Startup

CoinHarbor is a bitcoin brokerage in South Africa.
We need an advertisement for our Chatterly newsfeed.
Modern, technology feel to the advertisement.
Colours should compliment our logo in the attached document
Advertisement text: "The cheapest Bitcoin in South Africa"
Creative hints: Include an image of a bitcoin. Include something visual relating to South Africa (map, flag etc.). These are just hints an do not need to be followed to the letter, we appreciate creative freedom.
Updates

Project Deadline Extended Reason: This advertisement will only be needed on 10th May. Added Monday, April 24, 2017

Target Market(s)

People wanting to purchase bitcoin

Industry/Entity Type

News

Font styles to use
Sans Serif

Colors

Designer to choose colors to be used in the design.

Requirements
Must have
• Size: 1000 x 561 pixels (landscape)
• Text must not constitute more than 20% of the design (as per Chatterly requirements0
Nice to have
• Attached is our logo for your reference. Creative freedom is yours.
Should not have
• No preferences

Files

```html
<!DOCTYPE html>
<html lang="en">
<head>
<meta charset="utf-8">
<title>CoinHarbor – The Cheapest Bitcoin in South Africa</title>
<link rel="stylesheet" href="https://fonts.googleapis.com/css2?family=Open+Sans:wght@600;700;800&display=swap">
<style>
  :root {
    --stage: #2a2a2a;
    --sky-deep: #1c8ae6;
    --sky-mid: #3fa8f0;
    --sky-light: #d6ecfb;
    --paper: #eef6fc;
    --silver-hi: #f4f7fa;
    --silver: #c9d4de;
    --silver-lo: #8e9caa;
    --stack: #6f8aa3;
    --grid: #b8cfe2;
    --candle: #3d4a5a;
    --ink: #2f3640;
    --white: #ffffff;
    --amber: #f5a623;
  }
  * { margin: 0; padding: 0; box-sizing: border-box; }
  html, body {
    width: 1200px;
    height: 960px;
    overflow: hidden;
    background: var(--stage);
  }
  .ad {
    position: absolute;
    left: 60px;
    top: 177px;
    width: 1080px;
    height: 606px;
    overflow: hidden;
    font-family: "Open Sans", Arial, sans-serif;
    background: linear-gradient(100deg, var(--sky-deep) 0%, var(--sky-mid) 50%, #7cc4f4 100%);
    box-shadow: 0 10px 30px rgba(0,0,0,0.5);
  }
  .ad__table {
    position: absolute;
    inset: 0;
    background: linear-gradient(172deg, rgba(255,255,255,0) 62%, rgba(214,236,251,0.85) 78%, var(--paper) 100%);
  }
  .ad__chart {
    position: absolute;
    inset: 0;
    width: 1080px;
    height: 606px;
  }
  .ad__stacks {
    position: absolute;
    right: -30px;
    top: 20px;
    width: 200px;
    height: 520px;
    border-radius: 40px;
    background:
      radial-gradient(ellipse 110px 40px at 120px 300px, #7fe3ff 0%, rgba(127,227,255,0) 100%),
      linear-gradient(180deg, rgba(111,138,163,0.35) 0%, var(--stack) 55%, rgba(160,180,200,0.9) 100%);
    filter: blur(2px);
  }
  .ad__coin {
    position: absolute;
    left: 362px;
    top: 42px;
    width: 484px;
    height: 484px;
    border-radius: 50%;
    background:
      radial-gradient(circle at 42% 38%, var(--silver-hi) 0%, var(--silver) 55%, var(--silver-lo) 88%, #e8eef3 100%);
    box-shadow: 18px 22px 40px rgba(30,70,110,0.35), inset 0 0 0 10px rgba(255,255,255,0.55);
  }
  .brand {
    position: absolute;
    left: 65px;
    top: 52px;
    display: flex;
    align-items: center;
    gap: 18px;
  }
  .brand__mark {
    width: 50px;
    height: 50px;
    background: var(--amber);
    border-radius: 6px;
  }
  .brand__name {
    color: var(--white);
    font-weight: 700;
    font-size: 46px;
    letter-spacing: -0.5px;
  }
  .headline {
    position: absolute;
    left: 69px;
    top: 328px;
    line-height: 1.12;
    font-weight: 700;
  }
  .headline span { display: block; }
  .headline__the { color: var(--ink); font-size: 36px; font-weight: 800; }
  .headline__cheapest { color: var(--ink); font-size: 50px; font-weight: 700; }
  .headline__bitcoin { color: var(--white); font-size: 36px; margin-top: 4px; }
  .headline__country {
    color: var(--amber);
    font-size: 47px;
    font-weight: 800;
    margin-top: 6px;
    letter-spacing: 0.5px;
    text-shadow: 1px 1px 0 rgba(60,40,0,0.45);
  }
</style>
</head>
<body>
  <section class="ad">
    <div class="ad__table"></div>
    <svg class="ad__chart" viewBox="0 0 1080 606" aria-hidden="true">
      <g stroke="var(--grid)" stroke-width="1.5">
        <line x1="420" y1="606" x2="1080" y2="520"/>
        <line x1="600" y1="606" x2="1080" y2="560"/>
        <line x1="700" y1="520" x2="860" y2="606"/>
        <line x1="900" y1="470" x2="1040" y2="606"/>
      </g>
      <g stroke="var(--candle)" stroke-width="2" fill="var(--grid)">
        <line x1="528" y1="580" x2="528" y2="606"/><rect x="518" y="590" width="20" height="6"/>
        <line x1="607" y1="570" x2="607" y2="596"/><rect x="597" y="579" width="20" height="6"/>
        <line x1="681" y1="545" x2="681" y2="578"/><rect x="670" y="553" width="22" height="16"/>
        <line x1="741" y1="520" x2="741" y2="552"/><rect x="730" y="528" width="22" height="14"/>
        <line x1="829" y1="515" x2="829" y2="560"/><rect x="816" y="522" width="26" height="28"/>
        <line x1="917" y1="522" x2="917" y2="548"/><rect x="907" y="534" width="20" height="4"/>
        <line x1="967" y1="480" x2="967" y2="525"/><rect x="954" y="488" width="26" height="30" transform="rotate(-25 967 503)"/>
      </g>
    </svg>
    <div class="ad__stacks" role="img" aria-label="Blurred stacks of silver coins lit in cyan"></div>
    <div class="ad__coin" role="img" aria-label="Photo of a silver bitcoin coin standing upright on a price chart"></div>
    <div class="brand">
      <div class="brand__mark"></div>
      <span class="brand__name">CoinHarbor</span>
    </div>
    <h1 class="headline">
      <span class="headline__the">THE</span>
      <span class="headline__cheapest">Cheapest</span>
      <span class="headline__bitcoin">Bitcoin in</span>
      <span class="headline__country">SOUTH AFRICA</span>
    </h1>
  </section>
</body>
</html>
```